KB Rubbish Removal Business Card

Hey,
I need a double sided business card designed for a rubbish removal business based in Australia. Logo is already chosen, similar colours preferred for both sides of the business card.

Details to include:

Front:

KB Rubbish Removal
Darren Holloway
Managing Director
Mobile: 0471 902 146
Email: darren@kbrubbishremoval.com.au
Website: kbrubbishremoval.com.au

Rear:

How did we do?
kbrubbishremoval.com.au/review

```html
<!DOCTYPE html>
<html lang="en">
<head>
<meta charset="utf-8">
<title>KB Rubbish Removal – Business Card</title>
<link rel="stylesheet" href="https://fonts.googleapis.com/css2?family=Poppins:wght@300;400;600;700&display=swap">
<style>
  :root {
    --page: #f1f1f1;
    --card: #ffffff;
    --border: #2b2b2b;
    --brand: #22a447;
    --brand-dark: #168a36;
    --brand-deep: #0f7a2e;
    --ink: #222222;
    --ink-soft: #3a3a3a;
  }
  * { margin: 0; padding: 0; box-sizing: border-box; }
  html, body { width: 1200px; height: 1170px; overflow: hidden; background: var(--page); }
  body { position: relative; font-family: "Poppins", sans-serif; color: var(--ink); }

  .card {
    position: absolute; left: 140px; width: 920px; height: 553px;
    background: var(--card); border: 1.5px solid var(--border); overflow: hidden;
  }
  .card--front { top: 20px; }
  .card--back { top: 597px; }

  /* Front */
  .front-shapes { position: absolute; inset: 0; width: 100%; height: 100%; }
  .company-title {
    position: absolute; left: 36px; top: 228px;
    color: #fff; font-weight: 600; font-size: 46px; line-height: 1.3;
    letter-spacing: 2px; text-transform: uppercase;
  }
  .brand-mark {
    position: absolute; right: 52px; top: 128px;
    display: flex; align-items: center; gap: 10px;
    color: var(--brand); font-weight: 600; font-size: 22px;
  }
  .brand-mark__dot { width: 18px; height: 18px; border-radius: 50%; background: var(--brand); }
  .person { position: absolute; right: 49px; top: 270px; text-align: right; }
  .person__name {
    color: var(--brand); font-weight: 700; font-size: 31px; letter-spacing: 1.5px;
    text-transform: uppercase; line-height: 1.15;
  }
  .person__role { font-weight: 400; font-size: 21px; color: var(--ink-soft); line-height: 1.3; }
  .contacts { position: absolute; right: 53px; top: 382px; list-style: none; }
  .contacts li {
    display: flex; justify-content: flex-end; align-items: center; gap: 22px;
    height: 36px; margin-bottom: 15px;
    font-weight: 300; font-size: 21px; color: var(--ink);
  }
  .icon {
    width: 37px; height: 37px; background: var(--brand); flex: none;
    display: flex; align-items: center; justify-content: center;
  }
  .icon svg { width: 20px; height: 20px; fill: #fff; }

  /* Back */
  .review {
    position: absolute; inset: 0 0 36px 0;
    display: flex; flex-direction: column; align-items: center; justify-content: center;
    gap: 28px;
  }
  .review__title {
    color: var(--brand); font-weight: 700; font-size: 46px; letter-spacing: 1.5px;
    text-transform: uppercase;
  }
  .review__link {
    display: flex; align-items: center; gap: 18px;
    font-weight: 300; font-size: 26px; color: var(--ink);
  }
  .back-band {
    position: absolute; left: 0; right: 0; top: 517px; height: 12px;
    background: linear-gradient(90deg, var(--brand) 0%, var(--brand-deep) 50%, var(--brand) 100%);
  }
</style>
</head>
<body>

<section class="card card--front" aria-label="Business card front">
  <svg class="front-shapes" viewBox="0 0 682 410" preserveAspectRatio="none" aria-hidden="true">
    <defs>
      <linearGradient id="greenFill" x1="0" y1="0" x2="1" y2="1">
        <stop offset="0" stop-color="#a6d63a"/>
        <stop offset="0.55" stop-color="#6cc23f"/>
        <stop offset="1" stop-color="#2faf47"/>
      </linearGradient>
    </defs>
    <path d="M0 0 H342 C362 130 330 290 262 410 H0 Z" fill="#22a447"/>
    <path d="M0 0 H318 C346 140 316 300 244 410 H0 Z" fill="#168a36"/>
    <path d="M0 0 H282 C330 150 300 318 222 410 H0 Z" fill="url(#greenFill)"/>
  </svg>

  <h1 class="company-title">KB Rubbish<br>Removal</h1>

  <div class="brand-mark">
    <span class="brand-mark__dot"></span>
    <span>KB Rubbish Removal</span>
  </div>

  <div class="person">
    <p class="person__name">Darren Holloway</p>
    <p class="person__role">Managing Director</p>
  </div>

  <ul class="contacts">
    <li>0471 902 146
      <span class="icon"><svg viewBox="0 0 24 24"><path d="M6.6 10.8a15.1 15.1 0 0 0 6.6 6.6l2.2-2.2a1 1 0 0 1 1-.25 11.4 11.4 0 0 0 3.6.57 1 1 0 0 1 1 1V20a1 1 0 0 1-1 1A17 17 0 0 1 3 4a1 1 0 0 1 1-1h3.5a1 1 0 0 1 1 1c0 1.25.2 2.45.57 3.57a1 1 0 0 1-.25 1z"/></svg></span>
    </li>
    <li>darren@kbrubbishremoval.com.au
      <span class="icon"><svg viewBox="0 0 24 24"><path d="M3 5h18v14H3z" fill="none" stroke="#fff" stroke-width="2"/><path d="M3 5l9 7 9-7" fill="none" stroke="#fff" stroke-width="2"/></svg></span>
    </li>
    <li>kbrubbishremoval.com.au
      <span class="icon"><svg viewBox="0 0 24 24"><path d="M6 2l13 11h-6l3.5 7-2.5 1.2L10.5 14 6 18z"/></svg></span>
    </li>
  </ul>
</section>

<section class="card card--back" aria-label="Business card back">
  <div class="review">
    <h2 class="review__title">How did we do?</h2>
    <p class="review__link">
      <span class="icon"><svg viewBox="0 0 24 24"><path d="M6 2l13 11h-6l3.5 7-2.5 1.2L10.5 14 6 18z"/></svg></span>
      kbrubbishremoval.com.au/review
    </p>
  </div>
  <div class="back-band"></div>
</section>

</body>
</html>
```